main page images

We are looking for three splash images to promote our services and technology in the accommodation, hospital and aged care facilities. The look and feel would be preferred to look like the image below, but with the mentioned screens and products for each.

```html
<!DOCTYPE html>
<html lang="en">
<head>
<meta charset="utf-8">
<title>Corvana – Accommodation, Hospital and Aged Care</title>
<link href="https://fonts.googleapis.com/css2?family=Montserrat:wght@400;500;600;700&display=swap" rel="stylesheet">
<style>
  :root{
    --teal:#14878a;
    --teal-dark:#0f6f72;
    --marble-1:#f1f1f1;
    --marble-2:#dcdcdc;
    --stage:#b4b5b7;
    --white:#ffffff;
    --ink:#2b2b2b;
    --screen-grey:#a9a9ab;
    --screen-tint:#e9ebf3;
    --accent-blue:#2a6fd6;
  }
  *{box-sizing:border-box;margin:0;padding:0}
  html,body{width:806px;height:1200px;overflow:hidden}
  body{background:var(--stage);font-family:'Montserrat',sans-serif;color:var(--ink);position:relative}

  .poster{position:absolute;overflow:hidden;box-shadow:0 10px 14px -6px rgba(0,0,0,.35)}
  .poster--accommodation{left:125px;top:114px;width:558px;height:558px}
  .poster--hospital{left:46px;top:826px;width:323px;height:323px}
  .poster--aged-care{left:412px;top:826px;width:323px;height:323px}
  .poster__bg{position:absolute;inset:0;width:100%;height:100%}

  .poster__title{position:absolute;color:var(--white);font-weight:500;letter-spacing:.5px;white-space:nowrap}
  .poster--accommodation .poster__title{right:30px;top:54px;font-size:27px}
  .poster--hospital .poster__title,.poster--aged-care .poster__title{top:31px;font-size:15px;font-weight:600}
  .poster--hospital .poster__title{right:33px}
  .poster--aged-care .poster__title{right:23px}

  /* feature panel */
  .features{position:absolute;background:var(--teal);border-radius:26px 26px 0 0;display:grid;color:var(--white);font-weight:600;text-transform:uppercase}
  .poster--accommodation .features{left:28px;top:427px;width:501px;height:131px;grid-template-columns:241px 1fr;padding:15px 0 0 52px;font-size:12.3px;--lh:14.2px}
  .poster--hospital .features{left:16px;top:247px;width:290px;height:76px;grid-template-columns:140px 1fr;padding:6px 0 0 50px;font-size:6.8px;--lh:8.2px;border-radius:15px 15px 0 0}
  .poster--aged-care .features{left:16px;top:247px;width:290px;height:76px;grid-template-columns:113px 1fr;padding:18px 0 0 51px;font-size:6.8px;--lh:8.6px;border-radius:15px 15px 0 0}
  .features ul{list-style:none}
  .features li{position:relative;line-height:var(--lh);padding-left:1.15em;white-space:nowrap}
  .features li::before{content:"";position:absolute;left:0;top:50%;width:.62em;height:.62em;margin-top:-.31em;border:1px solid rgba(255,255,255,.85);border-radius:50%}
  .features li::after{content:"";position:absolute;left:.2em;top:50%;width:.3em;height:.16em;margin-top:-.14em;border-left:1px solid var(--white);border-bottom:1px solid var(--white);transform:rotate(-45deg)}

  /* TV (accommodation) */
  .tv{position:absolute;left:105px;top:88px;width:336px;height:191px;background:var(--white);border:2px solid #3a3a3a;border-bottom-width:3px}
  .tv__stand{position:absolute;left:105px;top:279px;width:336px;height:10px;background:linear-gradient(#d0d0d0,#9a9a9a)}
  .tv__foot{position:absolute;top:289px;width:6px;height:16px;background:#7c7c7c}
  .brand{position:absolute;font-weight:700;color:var(--ink);letter-spacing:.3px;white-space:nowrap}
  .tv .brand{left:12px;top:9px;font-size:9px}
  .status{position:absolute;white-space:nowrap}
  .status__time{font-weight:500}
  .status__meta{font-size:3.6px;line-height:1.5}
  .tv .status__time{position:absolute;left:276px;top:5px;font-size:7px}
  .tv .status__date{position:absolute;left:303px;top:5px}
  .tv .status__net{position:absolute;left:278px;top:18px}
  .tile{position:absolute}
  .tile--more{background:#c8c8c8;color:var(--white);font-size:3.6px;display:flex;align-items:center;justify-content:center}
  .nav{position:absolute;display:flex;text-align:center;color:var(--ink)}
  .nav__item{display:flex;flex-direction:column;align-items:center}
  .nav__item svg{fill:none;stroke:var(--ink);stroke-width:1.6}
  .tv .nav{left:52px;top:155px;gap:0}
  .tv .nav__item{width:44.7px;font-size:4px}
  .tv .nav__item svg{width:11px;height:11px;margin-bottom:3px}
  .tv .nav__arrow{position:absolute;left:278px;top:160px;width:6px;height:6px}

  .set-top{position:absolute;border-radius:3px}

  /* hospital annotated homepage */
  .homepage{position:absolute;left:21px;top:59px;width:281px;height:144px;background:var(--white);border-radius:8px}
  .homepage__label{position:absolute;left:12px;top:5px;font-size:7px;font-weight:500}
  .homepage__screen{position:absolute;left:25px;top:29px;width:171px;height:96px;background:var(--screen-tint)}
  .note{position:absolute;font-size:4.4px;white-space:nowrap}
  .leader{position:absolute;background:var(--accent-blue)}
  .leader--dot::after{content:"";position:absolute;right:-1px;top:-1px;width:2.4px;height:2.4px;border-radius:50%;background:var(--accent-blue)}
  .homepage .brand{font-size:5px}
  .homepage__text{position:absolute;left:112px;top:28px;width:53px;font-size:2.9px;line-height:1.35;text-align:justify;color:#1e1e1e}
  .homepage .nav{left:21px;top:84px}
  .homepage .nav__item{width:22.6px;font-size:2.2px}
  .homepage .nav__item svg{width:5px;height:5px;margin-bottom:1px;stroke-width:2}

  /* aged care tv */
  .room-tv{position:absolute;left:50px;top:58px;width:200px;height:141px;border:2px solid #222;background:#222}
  .room-tv__topbar{position:absolute;left:0;top:0;right:0;height:16px;background:var(--white);display:flex;align-items:center;padding:0 4px;font-size:6px;font-weight:600;white-space:nowrap}
  .room-tv__welcome{flex:1}
  .room-tv__temp{font-size:7px;font-weight:700;margin-right:4px}
  .room-tv__date{font-size:3.6px;line-height:1.15;border-right:1px solid #999;padding-right:3px;margin-right:3px;text-align:center}
  .room-tv__clock{font-size:8px;font-weight:700}
  .room-tv__clock small{font-size:3px}
  .room-tv__photo{position:absolute;left:0;right:0;top:16px;bottom:0;background:linear-gradient(180deg,#9fb9d6 0%,#c9d6e2 25%,#4f6b3b 48%,#2f4a24 72%,#6a8a6a 100%)}
  .room-tv .nav{left:10px;top:98px;gap:15px}
  .room-tv .nav__item{width:22px;height:22px;border-radius:50%;background:rgba(255,255,255,.35);border:1px solid rgba(255,255,255,.6);justify-content:center;font-size:3px;color:var(--white)}
  .room-tv .nav__item svg{width:8px;height:8px;stroke:var(--white);stroke-width:1.8}
  .room-tv__stand{position:absolute;left:60px;top:201px;width:180px;height:5px;background:linear-gradient(#e6e6e6,#8e8e8e)}
</style>
</head>
<body>

<!-- ACCOMMODATION -->
<section class="poster poster--accommodation">
  <svg class="poster__bg" viewBox="0 0 1085 1085" preserveAspectRatio="none" aria-hidden="true">
    <defs>
      <linearGradient id="marbleA" x1="0" y1="0" x2="1" y2="1">
        <stop offset="0" stop-color="#f3f3f3"/><stop offset=".5" stop-color="#e2e2e2"/><stop offset="1" stop-color="#d4d4d4"/>
      </linearGradient>
    </defs>
    <rect width="1085" height="1085" fill="url(#marbleA)"/>
    <path d="M0 38 H120 A115 115 0 0 1 120 268 H0 Z" fill="var(--teal)"/>
    <polygon points="757,0 1085,0 1085,370 0,640 0,310" fill="var(--teal)"/>
    <polygon points="1085,480 1085,640 0,820 0,760" fill="var(--teal)"/>
    <circle cx="900" cy="640" r="110" fill="var(--teal)"/>
  </svg>
  <h1 class="poster__title">ACCOMMODATION</h1>

  <div class="tv">
    <span class="brand">Corvana</span>
    <span class="status__time status">13 : 25</span>
    <span class="status status__date status__meta">2023-03-02<br>&nbsp;Thursday</span>
    <span class="status status__net status__meta">guestnet &nbsp;&nbsp; 20191212</span>

    <div class="tile" style="left:37px;top:34px;width:86px;height:118px;background:linear-gradient(160deg,#3c4f6a,#7a2a26 60%,#1d2230)" role="img" aria-label="Film poster artwork"></div>
    <div class="tile" style="left:125px;top:34px;width:102px;height:66px;background:linear-gradient(180deg,#6b6a8e,#c98e5c 55%,#2c2b35)" role="img" aria-label="Film poster artwork"></div>
    <div class="tile" style="left:125px;top:104px;width:50px;height:49px;background:linear-gradient(180deg,#dcd6c8,#9b7e5e)" role="img" aria-label="Film poster artwork"></div>
    <div class="tile" style="left:178px;top:104px;width:49px;height:49px;background:linear-gradient(180deg,#d8d6d2,#7a4a44)" role="img" aria-label="Film poster artwork"></div>
    <div class="tile" style="left:229px;top:34px;width:72px;height:104px;background:linear-gradient(180deg,#2e2a22,#8a6a3a 55%,#2a2418)" role="img" aria-label="Film poster artwork"></div>
    <div class="tile tile--more" style="left:229px;top:141px;width:72px;height:11px">More Movie</div>

    <nav class="nav">
      <span class="nav__item"><svg viewBox="0 0 24 24"><path d="M3 11 12 3l9 8M5 10v11h14V10"/></svg>Home</span>
      <span class="nav__item"><svg viewBox="0 0 24 24"><rect x="3" y="4" width="18" height="13"/><path d="M9 21h6M12 17v4"/></svg>Live</span>
      <span class="nav__item"><svg viewBox="0 0 24 24"><rect x="2" y="5" width="20" height="14"/><path d="M10 9l5 3-5 3z"/></svg>Movie</span>
      <span class="nav__item"><svg viewBox="0 0 24 24"><rect x="6" y="3" width="12" height="18"/><path d="M9 7h2M13 7h2M9 11h2M13 11h2M9 15h2M13 15h2"/></svg>Hotel</span>
      <span class="nav__item"><svg viewBox="0 0 24 24"><circle cx="8" cy="8" r="3"/><circle cx="16" cy="8" r="3"/><path d="M2 20c0-4 3-7 6-7s6 3 6 7M10 20c0-4 3-7 6-7s6 3 6 7"/></svg>Services</span>
    </nav>
    <svg class="nav__arrow" viewBox="0 0 10 10"><path d="M3 1l4 4-4 4" fill="none" stroke="#222" stroke-width="2"/></svg>
  </div>
  <div class="tv__stand"></div>
  <div class="tv__foot" style="left:130px"></div>
  <div class="tv__foot" style="left:410px"></div>

  <div class="set-top" style="left:107px;top:325px;width:154px;height:47px;background:linear-gradient(180deg,#ecebf2 0%,#ecebf2 35%,#2a2a2a 36%,#2a2a2a 55%,#f3f3f6 56%)" role="img" aria-label="Set-top box, front view"></div>
  <div class="set-top" style="left:286px;top:324px;width:153px;height:49px;background:linear-gradient(180deg,#f1f0f5 0%,#e6e6ea 45%,#c9c9cf 100%)" role="img" aria-label="Set-top box, rear ports view"></div>

  <div class="features">
    <ul><li>RTLS</li><li>Guest Wi-Fi</li><li>Tablets</li><li>BYOD</li><li>Digital Signage</li><li>Information Kiosks</li></ul>
    <ul><li>Food Ordering</li><li>Onscreen Check Out</li><li>Reporting</li><li>EOC</li><li>AUDIOSYNC</li><li>IOT</li></ul>
  </div>
</section>

<!-- HOSPITAL -->
<section class="poster poster--hospital">
  <svg class="poster__bg" viewBox="0 0 1085 1085" preserveAspectRatio="none" aria-hidden="true">
    <defs>
      <linearGradient id="marbleH" x1="0" y1="0" x2="1" y2="1">
        <stop offset="0" stop-color="#f3f3f3"/><stop offset=".5" stop-color="#e2e2e2"/><stop offset="1" stop-color="#d4d4d4"/>
      </linearGradient>
    </defs>
    <rect width="1085" height="1085" fill="url(#marbleH)"/>
    <path d="M0 38 H120 A115 115 0 0 1 120 268 H0 Z" fill="var(--teal)"/>
    <polygon points="757,0 1085,0 1085,370 0,640 0,310" fill="var(--teal)"/>
    <polygon points="1085,480 1085,640 0,830 0,760" fill="var(--teal)"/>
    <circle cx="880" cy="660" r="110" fill="var(--teal)"/>
  </svg>
  <h2 class="poster__title">HOSPITAL</h2>

  <div class="homepage">
    <span class="homepage__label">HOMEPAGE</span>
    <span class="note" style="left:31px;top:18px">Custom Logo</span>
    <span class="leader" style="left:45px;top:23px;width:1px;height:9px"></span>

    <div class="homepage__screen">
      <span class="brand" style="left:13px;top:3px">Corvana</span>
      <span class="status" style="left:142px;top:3px;font-size:4px">13 : 25</span>
      <span class="status status__meta" style="left:155px;top:2px;font-size:1.8px">2023-03-02<br>Thursday</span>
      <div class="tile" style="left:2px;top:14px;width:106px;height:68px;background:linear-gradient(180deg,#c9d3e2,#e8edf3 40%,#7fa6c8 70%,#b9c4d2)" role="img" aria-label="Hospital ward photograph"></div>
      <div class="tile" style="left:112px;top:14px;width:59px;height:68px;background:var(--screen-grey)"></div>
      <span class="brand" style="left:132px;top:15px;font-size:4.5px">Corvana</span>
      <p class="homepage__text">Welcome to your room. Scan the code for Wi-Fi, menus and care team updates. Ask staff if you need help with anything today.</p>
      <nav class="nav">
        <span class="nav__item"><svg viewBox="0 0 24 24"><path d="M3 11 12 3l9 8M5 10v11h14V10"/></svg>Home</span>
        <span class="nav__item"><svg viewBox="0 0 24 24"><rect x="3" y="4" width="18" height="13"/><path d="M9 21h6M12 17v4"/></svg>Live</span>
        <span class="nav__item"><svg viewBox="0 0 24 24"><rect x="2" y="5" width="20" height="14"/><path d="M10 9l5 3-5 3z"/></svg>Movie</span>
        <span class="nav__item"><svg viewBox="0 0 24 24"><rect x="6" y="3" width="12" height="18"/><path d="M9 7h2M13 7h2M9 11h2M13 11h2"/></svg>Hotel</span>
        <span class="nav__item"><svg viewBox="0 0 24 24"><circle cx="8" cy="8" r="3"/><circle cx="16" cy="8" r="3"/><path d="M2 20c0-4 3-7 6-7s6 3 6 7M10 20c0-4 3-7 6-7s6 3 6 7"/></svg>Services</span>
        <span class="nav__item" style="font-size:5px;justify-content:center">›</span>
      </nav>
    </div>

    <span class="leader leader--dot" style="left:180px;top:40px;width:22px;height:1px"></span>
    <span class="note" style="left:205px;top:38px">Custom Wifi name &amp; password</span>
    <span class="leader leader--dot" style="left:168px;top:47px;width:34px;height:1px"></span>
    <span class="note" style="left:205px;top:45px">Custom Logo</span>
    <span class="leader leader--dot" style="left:180px;top:62px;width:22px;height:1px"></span>
    <span class="note" style="left:205px;top:60px">Custom Text</span>
    <span class="leader leader--dot" style="left:180px;top:95px;width:22px;height:1px"></span>
    <span class="note" style="left:205px;top:93px">Custom QR Code</span>

    <span class="leader" style="left:32px;top:111px;width:1px;height:22px"></span>
    <span class="note" style="left:26px;top:134px">Custom Picture &amp; Videos</span>
  </div>

  <div class="features">
    <ul><li>RTLS</li><li>Patient Wi-Fi</li><li>Tablets</li><li>BYOD</li><li>Digital Signage</li><li>Information Kiosks</li><li>Food Ordering</li></ul>
    <ul><li>CAREPANEL</li><li>eConcierge</li><li>Multilingual</li><li>Surveys</li><li>Reporting</li><li>Telephony</li><li>IOT</li></ul>
  </div>
</section>

<!-- AGED CARE -->
<section class="poster poster--aged-care">
  <svg class="poster__bg" viewBox="0 0 1085 1085" preserveAspectRatio="none" aria-hidden="true">
    <defs>
      <linearGradient id="marbleC" x1="0" y1="0" x2="1" y2="1">
        <stop offset="0" stop-color="#f3f3f3"/><stop offset=".5" stop-color="#e2e2e2"/><stop offset="1" stop-color="#d4d4d4"/>
      </linearGradient>
    </defs>
    <rect width="1085" height="1085" fill="url(#marbleC)"/>
    <path d="M0 38 H120 A115 115 0 0 1 120 268 H0 Z" fill="var(--teal)"/>
    <polygon points="757,0 1085,0 1085,370 0,640 0,310" fill="var(--teal)"/>
    <polygon points="1085,480 1085,640 0,830 0,760" fill="var(--teal)"/>
    <circle cx="900" cy="650" r="110" fill="var(--teal)"/>
  </svg>
  <h2 class="poster__title">AGED CARE</h2>

  <div class="room-tv">
    <div class="room-tv__photo" role="img" aria-label="Tropical coastal mountain landscape photograph"></div>
    <div class="room-tv__topbar">
      <span class="room-tv__welcome">Welcome Ruth &amp; Owen</span>
      <span class="room-tv__temp">20°C</span>
      <span class="room-tv__date">Tuesday<br>31st July</span>
      <span class="room-tv__clock">5:00<small>pm</small></span>
    </div>
    <nav class="nav">
      <span class="nav__item"><svg viewBox="0 0 24 24"><path d="M3 11 12 3l9 8M5 10v11h14V10"/></svg>Home</span>
      <span class="nav__item"><svg viewBox="0 0 24 24"><rect x="3" y="4" width="18" height="13"/><path d="M9 21h6M12 17v4"/></svg>Live</span>
      <span class="nav__item"><svg viewBox="0 0 24 24"><rect x="2" y="5" width="20" height="14"/><path d="M10 9l5 3-5 3z"/></svg>Movie</span>
      <span class="nav__item"><svg viewBox="0 0 24 24"><rect x="6" y="3" width="12" height="18"/><path d="M9 7h2M13 7h2M9 11h2M13 11h2"/></svg>Hotel</span>
      <span class="nav__item"><svg viewBox="0 0 24 24"><circle cx="8" cy="8" r="3"/><circle cx="16" cy="8" r="3"/><path d="M2 20c0-4 3-7 6-7s6 3 6 7M10 20c0-4 3-7 6-7s6 3 6 7"/></svg>Services</span>
    </nav>
  </div>
  <div class="room-tv__stand"></div>

  <div class="features">
    <ul><li>Streaming</li><li>RTLS</li><li>Guest Wi-Fi</li><li>Digital Signage</li></ul>
    <ul><li>Information Kiosks</li><li>Food Ordering</li><li>Multilingual</li><li>Reporting</li></ul>
  </div>
</section>

</body>
</html>
```